New Template design for Website in Wordpress

We are interested in changing our website look at www.cargolinx.com -We also are very interested in Have it done in Wordpress in which we are understanding the search engines are liking a bit more. The website we would want to try working with on this is www.cargolinx.com. We look forward to seeing the different design ideas please just make sure they are in wordpress! Thanks, Marlen

Reason: need more design idea..... We would still like to use our pictures off our site since we paid for them so keep that in mind as well as we would still want the rotating pictures in the head of the page but not in Flash.

```html
<!DOCTYPE html>
<html lang="en">
<head>
<meta charset="utf-8">
<title>CargoLinx – Home</title>
<link rel="stylesheet" href="https://fonts.googleapis.com/css2?family=Open+Sans:wght@400;600;700&display=swap">
<style>
:root{
  --red:#8a0f0b;
  --red-dark:#6e0a08;
  --navy:#1c2740;
  --navy-2:#27344f;
  --cyan:#29b6e6;
  --yellow:#f8c21d;
  --yellow-edge:#e0a90f;
  --ink:#222;
  --muted:#666;
  --soft:#f5f5f5;
  --line:#d8d8d8;
  --footer:#2a2a2a;
}
*{box-sizing:border-box;margin:0;padding:0}
html,body{width:890px;height:1200px;overflow:hidden}
body{position:relative;background:#fff;font-family:"Open Sans",Arial,sans-serif;color:var(--ink)}
.abs{position:absolute}
.topline{left:0;top:0;width:890px;height:3px;background:#111}

.brand{left:82px;top:26px}
.brand-name{font-size:27px;font-weight:700;color:var(--red);letter-spacing:.5px;line-height:30px}
.brand-tag{font-size:13px;color:#333;letter-spacing:.3px;line-height:15px}

.quote-btn{left:649px;top:16px;width:159px;height:33px;background:var(--cyan);color:#fff;font-size:12px;display:flex;align-items:center;justify-content:center;gap:7px}
.quote-btn b{font-weight:700}
.care{right:82px;top:58px;font-size:11.5px;font-weight:600;color:#333;display:flex;align-items:center;gap:6px}
.care em{font-style:normal;color:var(--red)}

.nav{left:0;top:91px;width:890px;height:33px;background:linear-gradient(var(--navy-2),var(--navy))}
.nav a{position:absolute;top:0;height:33px;line-height:33px;color:#fff;font-size:11.5px;font-weight:600;text-decoration:none}
.nav a.active{background:#fff;color:var(--red);font-weight:700;padding:0 9px}
.social{right:98px;top:8px;display:flex;gap:9px}
.social span{width:17px;height:17px;border-radius:50%;background:#3a4762;border:1px solid #55627c}

.hero{left:0;top:124px;width:890px;height:352px;background:linear-gradient(170deg,#5f7f9f 0%,#3d6689 45%,#4b7497 70%,#7c9bb6 100%)}
.hero-ship{left:375px;top:45px;width:460px;height:250px;background:linear-gradient(160deg,#c9ced4 0%,#b52a2e 40%,#8e1c20 60%,#d8dde2 90%);opacity:.55;border-radius:4px}
.caption{left:82px;top:223px;width:298px;height:115px;background:rgba(255,255,255,.93);padding:16px 17px}
.caption h1{font-size:16.5px;font-weight:400;line-height:20px;color:var(--navy)}
.caption h1 span{color:var(--red)}
.caption .cta{margin-top:11px;width:180px;height:29px;background:var(--red);color:#fff;font-size:11px;display:flex;align-items:center;justify-content:center;gap:9px}
.dots{left:102px;top:350px;display:flex;gap:2px}
.dots i{width:6px;height:6px;border-radius:50%;background:#fff}
.dots i:first-child{background:var(--red)}

.card{top:436px;height:175px;background:#fff;box-shadow:0 3px 8px rgba(0,0,0,.12)}
.card-head{height:40px;border-bottom:1px solid #e6e6e6;display:flex;align-items:center;gap:9px;padding-left:17px;font-size:11.5px;line-height:13px;color:#222}
.card-body{padding:12px 12px 0 12px;font-size:9.5px;line-height:11.8px;color:#444;height:95px}
.card-more{padding-left:12px;font-size:10px;color:var(--red);text-decoration:underline}
.card-more::after{content:" →";text-decoration:none;font-size:9px}
.card.featured{background:var(--red);box-shadow:none}
.card.featured .card-head{border-color:transparent;color:#fff;padding-left:25px}
.card.featured .card-body{color:#fff;padding-left:18px}
.card.featured .card-more{display:inline-block;margin-left:19px;padding:4px 8px;background:var(--navy);color:#fff}

.works{left:0;top:618px;width:890px;height:525px;background:var(--soft)}
.works h2{position:absolute;top:50px;width:890px;text-align:center;font-size:31px;font-weight:400;color:var(--red);letter-spacing:-.5px}
.works .rule{position:absolute;left:332px;top:94px;width:220px;height:3px;background:#ccc}
.works p{position:absolute;left:163px;width:564px;text-align:center;font-size:10px;line-height:13.4px;color:#666}
.learn{left:378px;top:269px;width:132px;height:36px;background:var(--yellow);border-bottom:3px solid var(--yellow-edge);font-size:11.5px;color:#222;display:flex;align-items:center;justify-content:center}

.tabs{left:0;top:962px;width:890px;height:33px;border-bottom:1px solid var(--line)}
.tab{position:absolute;height:25px;top:7px;background:linear-gradient(#fff,#ececec);border:1px solid var(--line);border-bottom:none;font-size:10.5px;color:#333;display:flex;align-items:center;justify-content:center}
.tab.current{top:0;height:32px;background:var(--red);border-color:var(--red);color:#fff;font-weight:700;font-size:12px;gap:7px}
.lists{left:0;top:995px;width:890px;height:148px;background:#fff}
.lists ul{position:absolute;top:16px;list-style:none;font-size:9.5px;line-height:11.7px;color:#888}
.lists ul.main{color:#111}

.footer{left:0;top:1143px;width:890px;height:57px;background:var(--footer);color:#aaa;font-size:9.5px;line-height:12.5px}
.footer .addr{position:absolute;left:83px;top:18px}
.footer .copy{position:absolute;right:83px;top:18px}
</style>
</head>
<body>
<div class="abs topline"></div>

<header>
  <div class="abs brand">
    <div class="brand-name">CARGOLINX</div>
    <div class="brand-tag">A MULTIMODAL FREIGHT COMPANY</div>
  </div>
  <div class="abs quote-btn">
    <svg width="16" height="16" viewBox="0 0 16 16"><path d="M8 1l6 3v8l-6 3-6-3V4z" fill="none" stroke="#fff" stroke-width="1.5"/><path d="M2 4l6 3 6-3M8 7v8" stroke="#fff" stroke-width="1.3" fill="none"/></svg>
    <span>GET A <b>FREIGHT QUOTE</b></span>
  </div>
  <div class="abs care">
    <svg width="8" height="12" viewBox="0 0 8 12"><path d="M6 1C3 1 1 3 1 6s2 5 5 5" stroke="#222" stroke-width="2.2" fill="none"/></svg>
    <span><em>CUSTOMER</em> CARE (888) 555-0142</span>
  </div>
</header>

<nav class="abs nav">
  <a class="active" style="left:87px">HOME</a>
  <a style="left:159px">INSURANCE &amp; LEGAL INFO</a>
  <a style="left:332px">FAST FREIGHT QUOTE</a>
  <div class="abs social"><span></span><span></span><span></span><span></span></div>
</nav>

<section class="abs hero" role="img" aria-label="Photo of a container ship loaded with red cargo containers sailing on open sea">
  <div class="abs hero-ship"></div>
</section>
<div class="abs caption">
  <h1>Worldwide Shipping Trucking <span>and</span><br><span>Ocean Service with No Limits</span></h1>
  <div class="cta">Click Here for Freight Quote
    <svg width="16" height="16" viewBox="0 0 16 16"><circle cx="8" cy="8" r="7" fill="#fff"/><path d="M4 8h7M8 5l3 3-3 3" stroke="#8a0f0b" stroke-width="1.8" fill="none"/></svg>
  </div>
</div>
<div class="abs dots"><i></i><i></i><i></i><i></i></div>

<article class="abs card featured" style="left:82px;width:170px">
  <div class="card-head">
    <svg width="18" height="16" viewBox="0 0 18 16"><rect x="3" y="2" width="12" height="8" rx="2" fill="#fff"/><rect x="1" y="9" width="16" height="4" fill="#fff"/><circle cx="5" cy="14" r="2" fill="#fff"/><circle cx="13" cy="14" r="2" fill="#fff"/></svg>
    Heavy Haul
  </div>
  <div class="card-body">Welcome to CargoLinx.com heavy haul services.We are shipping equipment daily whether 5000LB LTL machin-ery or 200,000 LB equipment from door to door.</div>
  <a class="card-more">Read More</a>
</article>
<article class="abs card" style="left:270px;width:171px">
  <div class="card-head">
    <svg width="26" height="18" viewBox="0 0 26 18"><rect x="1" y="3" width="15" height="10" fill="#8a0f0b"/><path d="M16 6h5l4 4v3h-9z" fill="#1c2740"/><circle cx="6" cy="15" r="2.5" fill="#1c2740"/><circle cx="20" cy="15" r="2.5" fill="#1c2740"/></svg>
    Dry &amp; Refrigerated
  </div>
  <div class="card-body">We currently offer dry van / box van service to all 48 States and Canada. Our Dry Van lengths start at 24' and go up to 53' in length.</div>
  <a class="card-more">Read More</a>
</article>
<article class="abs card" style="left:453px;width:170px">
  <div class="card-head" style="padding-left:11px">
    <svg width="34" height="20" viewBox="0 0 34 20"><path d="M3 3h2v13H3zM5 15h12" stroke="#1c2740" stroke-width="2" fill="none"/><rect x="8" y="6" width="8" height="7" fill="#8a0f0b"/><circle cx="10" cy="17" r="2" fill="#1c2740"/><circle cx="18" cy="17" r="2" fill="#1c2740"/><path d="M22 15h10" stroke="#1c2740" stroke-width="2"/></svg>
    Flatbed, Step Deck &amp;<br>Piggy back
  </div>
  <div class="card-body">With thousands of flatbeds transporting freight for our customers from coast to coast, we provide some of the most competitive rates</div>
  <a class="card-more">Read More</a>
</article>
<article class="abs card" style="left:638px;width:171px">
  <div class="card-head">
    <svg width="22" height="22" viewBox="0 0 22 22"><rect x="8" y="2" width="6" height="5" fill="#8a0f0b"/><rect x="5" y="7" width="12" height="5" fill="#1c2740"/><path d="M1 12h20l-4 7H5z" fill="#1c2740"/><path d="M1 21c3-2 5 0 7-1s4-1 6 0 5 0 7-1" stroke="#1c2740" stroke-width="1.2" fill="none"/></svg>
    Freight Forwarding<br>Ocean
  </div>
  <div class="card-body">Welcome to CargoLinx.com heavy haul services.We are shipping equipment daily whether 5000LB LTL ma-chinery or 200,000 LB</div>
  <a class="card-more">Read More</a>
</article>

<section class="abs works">
  <h2>How CargoLinx Works</h2>
  <div class="rule"></div>
  <p style="top:122px">Welcome to CargoLinx and Meridian Haulage Inc. We are a one stop solution logistics company servicing Worldwide with our Trucking and Ocean shipping service. In using our freight services, we will negotiate a competitive freight quote using over 5000 different carriers who are certified and contracted by us. We have all equipment types available daily, service all freight types, and have no limits Worldwide.</p>
  <p style="top:189px">Whether you need a freight quote for a full load, LTL/Partial load, or Oversized Machinery or Equipment, trucking and/or ocean shipment, we will take care of it. All your freight or equipment to be shipped will be covered in full by our insurance with no limitations to match its value. We manage the calls, the paperwork, and the headaches, and you get your freight moved with no hassles at a competitive shipping price!</p>
  <div class="abs learn">Learn More about Us</div>
</section>

<div class="abs tabs">
  <div class="tab current" style="left:82px;width:173px">
    <svg width="13" height="13" viewBox="0 0 13 13" fill="#fff"><rect x="0" y="0" width="3" height="3"/><rect x="5" y="0" width="3" height="3"/><rect x="10" y="0" width="3" height="3"/><rect x="0" y="5" width="3" height="3"/><rect x="5" y="5" width="3" height="3"/><rect x="10" y="5" width="3" height="3"/><rect x="0" y="10" width="3" height="3"/><rect x="5" y="10" width="3" height="3"/><rect x="10" y="10" width="3" height="3"/></svg>
    CATEGORIES
  </div>
  <div class="tab" style="left:262px;width:173px">Freight Services</div>
  <div class="tab" style="left:442px;width:173px">Truck Types Available</div>
  <div class="tab" style="left:621px;width:173px">We Ship It All!</div>
</div>

<section class="abs lists">
  <ul class="main" style="left:96px"><li>Freight Services</li><li>Truck Types Available</li><li>We Ship It All!</li></ul>
  <ul style="left:268px"><li>Freight Service Areas</li><li>Truck Equipment Types</li><li>Insurance &amp; Legal Details</li><li>Get a Freight Quote Now!</li><li>Return to Home Page</li></ul>
  <ul style="left:445px"><li>Heavy Equipment Hauling</li><li>LTL Freight Transport</li><li>Flatbed Transport</li><li>Step Deck Transport</li><li>Dry Van Transport</li><li>Refrigerated Transport</li><li>Power Only &amp; Towaway Transport</li></ul>
  <ul style="left:624px"><li>Full Loads</li><li>LTL-Less Then Full Loads</li><li>Oversized &amp; Overweight Loads</li><li>500 LBS to 200,000 LBS (No Limits)</li><li>Construction &amp; Mining Equipment</li><li>Mills &amp; Machinery</li><li>Hay &amp; Alfalfa</li><li>Agriculture Equipment &amp; Commodities More</li></ul>
</section>

<footer class="abs footer">
  <div class="addr">CargoLinx | Address: 1480 Harbor View Road, Portside, CA 90210<br>E-mail: sales@cargolinx.com | Phone +888 555-0142 | Fax (888) 555-0143</div>
  <div class="copy">Copyright and Owned by Meridian Haulage Inc. and CargoLinx.com</div>
</footer>
</body>
</html>
```